Label to go onto food packaging.

We need to create a visually interesting and appealing label to stick onto our take away food packaging. The label should contain information of the food products our cafe sells. The label is to go onto biodegradable food bowls and clam shell packaging.
The information is basically the lines we sell - buddha bowls, super smoothies, vegan burgers and curries. And also the slogan 'nourish and refresh'. We have a logo design that we would like to incorporate onto the label (but not essential)
The design will go onto a rectangle strip label.
The colours of our food outlet are splashes of yellow, blue and grey in a white interior.
We also feature a large garden green wall. You may view images from our instagram page quiet pebble kitchen

Target Market(s)

Young professional, health conscious, plant based eaters. To be used on takeaway packaging.

Industry/Entity Type

Food Production

Font styles to use
Sans Serif

Colors

Designer to choose colors to be used in the design.

Requirements
Must have
• Bold, appealing, informative.
Nice to have
• Logo incorporated, possibly as a watermark?
Should not have
• No floral shapes. If incorporating the logo, use a circle or nothing around it. No pictures/photos of food

```html
<!DOCTYPE html>
<html lang="en">
<head>
<meta charset="utf-8">
<title>Quiet Pebble Kitchen – Vegan Burger Labels</title>
<link href="https://fonts.googleapis.com/css2?family=Fira+Sans:wght@800&family=Montserrat:wght@700&family=Playball&display=swap" rel="stylesheet">
<style>
  :root{
    --page:#ffffff;
    --ink:#231f20;
    --green:#8dc63f;
    --slate:#6b747c;
    --lemon:#fff352;
    --sun:#ffd200;
  }
  html,body{margin:0;padding:0;overflow:hidden;background:var(--page);}
  .canvas{position:relative;width:1200px;height:1000px;overflow:hidden;background:var(--page);}
  .label-row{position:absolute;left:0;width:1200px;height:231px;}
  .row-1{top:110px}.row-2{top:385px}.row-3{top:659px}

  .brand-mark{position:absolute;left:205px;top:38px;width:156px;height:156px;}
  .brand-mark circle{fill:none;stroke:var(--ink);stroke-width:4;}
  .brand-name{position:absolute;left:205px;top:38px;width:156px;height:156px;display:flex;align-items:center;justify-content:center;text-align:center;
    font-family:'Montserrat',sans-serif;font-weight:700;font-size:15px;line-height:1.15;color:var(--ink);text-transform:uppercase;letter-spacing:.5px;}

  .strip{position:absolute;left:360px;top:0;width:672px;height:231px;}
  .strip-green{background:var(--green);}
  .strip-slate{background:var(--slate);}
  .strip-lemon{background:var(--lemon);}
  .brace{position:absolute;left:360px;top:0;width:70px;height:231px;}
  .brace .edge{fill:var(--page);}
  .brace .bar{fill:none;stroke:var(--ink);stroke-width:16;stroke-linejoin:round;}

  .copy{position:absolute;left:430px;top:0;width:562px;height:231px;text-align:center;color:var(--ink);}
  .copy-sun{color:var(--sun);}
  .slogan{position:absolute;left:0;right:0;top:46px;margin:0;font-family:'Montserrat',sans-serif;font-weight:700;font-size:25px;letter-spacing:.5px;}
  .product{position:absolute;left:0;right:0;top:76px;margin:0;font-family:'Fira Sans',sans-serif;font-weight:800;font-size:70px;line-height:1;letter-spacing:.5px;}
  .tagline{position:absolute;left:0;right:0;top:168px;margin:0;font-family:'Playball',cursive;font-size:25px;}
</style>
</head>
<body>
<div class="canvas">

  <section class="label-row row-1">
    <svg class="brand-mark" viewBox="0 0 156 156"><circle cx="78" cy="78" r="74"/></svg>
    <div class="brand-name">Quiet<br>Pebble<br>Kitchen</div>
    <div class="strip strip-green"></div>
    <svg class="brace" viewBox="0 0 70 231">
      <path class="bar" d="M0,8 C24,8 36,18 36,42 V98 C36,108 42,113 52,115.5 C42,118 36,123 36,133 V189 C36,213 24,223 0,223"/>
      <path class="edge" d="M0,0 C20,0 28,14 28,40 V98 C28,106 32,112 38,115.5 C32,119 28,125 28,133 V191 C28,217 20,231 0,231 Z"/>
    </svg>
    <div class="copy">
      <p class="slogan">NOURISH &amp; REFRESH</p>
      <h1 class="product">Vegan Burger</h1>
      <p class="tagline">Nutrient dense whole foods</p>
    </div>
  </section>

  <section class="label-row row-2">
    <svg class="brand-mark" viewBox="0 0 156 156"><circle cx="78" cy="78" r="74"/></svg>
    <div class="brand-name">Quiet<br>Pebble<br>Kitchen</div>
    <div class="strip strip-slate"></div>
    <svg class="brace" viewBox="0 0 70 231">
      <path class="bar" d="M0,8 C24,8 36,18 36,42 V98 C36,108 42,113 52,115.5 C42,118 36,123 36,133 V189 C36,213 24,223 0,223"/>
      <path class="edge" d="M0,0 C20,0 28,14 28,40 V98 C28,106 32,112 38,115.5 C32,119 28,125 28,133 V191 C28,217 20,231 0,231 Z"/>
    </svg>
    <div class="copy copy-sun">
      <p class="slogan">NOURISH &amp; REFRESH</p>
      <h2 class="product">Vegan Burger</h2>
      <p class="tagline">Nutrient dense whole foods</p>
    </div>
  </section>

  <section class="label-row row-3">
    <svg class="brand-mark" viewBox="0 0 156 156"><circle cx="78" cy="78" r="74"/></svg>
    <div class="brand-name">Quiet<br>Pebble<br>Kitchen</div>
    <div class="strip strip-lemon"></div>
    <svg class="brace" viewBox="0 0 70 231">
      <path class="bar" d="M0,8 C24,8 36,18 36,42 V98 C36,108 42,113 52,115.5 C42,118 36,123 36,133 V189 C36,213 24,223 0,223"/>
      <path class="edge" d="M0,0 C20,0 28,14 28,40 V98 C28,106 32,112 38,115.5 C32,119 28,125 28,133 V191 C28,217 20,231 0,231 Z"/>
    </svg>
    <div class="copy">
      <p class="slogan">NOURISH &amp; REFRESH</p>
      <h2 class="product">Vegan Burger</h2>
      <p class="tagline">Nutrient dense whole foods</p>
    </div>
  </section>

</div>
</body>
</html>
```